Webdesign für Lösungsanbieter für die Digitalisierung von Unternehmen
Zielgruppe
Wir sehen uns als Ihr Lösungsanbieter für die Digitalisierung Ihres Unternehmens. Durch unser breit aufgestelltes Leistungsportfolio sind wird in der Lage Sie mit Komplettlösungen im Bereich Bürokommunikation und Infrastruktur zu unterstützen.
Wir wünschen uns ein neues frisches Design, gerne etwas unkonventionell. Unsere Zielgruppe sind kleine bis Mittelständige Unternehmen. Labore sind die Zielgruppe für unsere eigenen Produkte. Des weiteren betreuen wir deutschlandweit Kunden im Cloudbereich und IP Telefonie.
Unsere Tätigkeit
- IT Systemhaus (Verkauf und Installation von IT Systemem)
- Softwareentwicklung (eingene Produkte sowie Auftragsentwicklungen für Kunden)
- IP Telefonsysteme
- Sicherheitstechnik
- Clouddiesnste (Rechnenzentrum, SaaS,IAAS)
- Webhosting
- Consulting
- Netzwerktechnik (Glasfaser und Kupfer).
Aufgabenstellung
Wir bitten um offene Daten.

```html
<!DOCTYPE html>
<html lang="de">
<head>
<meta charset="utf-8">
<title>nexora – IT Solutions</title>
<link href="https://fonts.googleapis.com/css2?family=Oswald:wght@500;600&family=Roboto:wght@300;400;500;700&family=Barlow+Condensed:wght@400&display=swap" rel="stylesheet">
<style>
:root{
  --navy:#15152b;
  --navy-2:#1c1d36;
  --orange:#e8821f;
  --green:#b5c23a;
  --grey:#f2f2f2;
  --line:#dedede;
  --text:#222;
  --muted:#555;
}
*{box-sizing:border-box;margin:0;padding:0}
html,body{width:1200px;height:3641px;overflow:hidden}
body{font-family:'Roboto',sans-serif;color:var(--text);background:#fff;position:relative}
section,header,footer{position:relative;width:1200px;overflow:hidden}
.eyebrow{font-size:12px;text-transform:uppercase;color:var(--orange);letter-spacing:.2px}
.title{font-weight:700;text-transform:uppercase;font-size:19px;color:#222}
.btn{display:inline-block;background:var(--orange);color:#fff;border-radius:18px;font-size:11px;padding:8px 18px}
.brand{font-family:'Roboto',sans-serif;font-weight:300;color:var(--green);letter-spacing:1px;display:flex;align-items:center;gap:12px}
.brand .dot{width:40px;height:40px;border-radius:50%;background:var(--orange)}

/* Hero */
.hero{height:445px;background:var(--navy)}
.hero-visual{position:absolute;right:0;top:0;width:700px;height:438px;background:radial-gradient(ellipse at 60% 45%,#2f6aa8 0%,#1d3b66 35%,#15152b 75%)}
.hero-base{position:absolute;left:0;bottom:0;width:100%;height:7px;background:#4b4c5c}
.hero .brand{position:absolute;left:174px;top:34px;font-size:44px}
.nav{position:absolute;left:535px;top:56px;display:flex;gap:25px;align-items:center;font-size:11px;color:#fff;text-transform:uppercase}
.nav .active{color:var(--green)}
.nav .kontakt{background:var(--orange);padding:9px 16px;margin-left:3px}
.hero-copy{position:absolute;left:174px;top:152px;width:420px;color:#fff}
.hero-copy .eyebrow{color:var(--green);font-size:11px}
.hero-copy h1{font-family:'Oswald',sans-serif;font-weight:600;font-size:47px;line-height:52px;margin-top:8px;text-transform:uppercase}
.hero-copy p{font-size:12px;line-height:17px;color:#c9c9d4;margin-top:12px;width:280px}

/* Services */
.services{height:827px}
.section-head{text-align:center;padding-top:105px}
.section-head .title{margin-top:8px}
.service-grid{position:absolute;left:174px;top:205px;display:grid;grid-template-columns:repeat(4,208px);grid-auto-rows:266px;column-gap:7px;row-gap:15px}
.card{border:1px solid var(--line);text-align:center;background:#fff}
.card .media{height:115px}
.card h3{font-size:11px;font-weight:500;margin-top:19px;text-transform:uppercase}
.card p{font-size:8.5px;line-height:12.5px;color:var(--muted);padding:0 22px;margin-top:10px}
.card .more{display:inline-block;margin-top:18px;border:1px solid var(--orange);color:var(--orange);font-size:8.5px;padding:6px 14px}

/* CTA */
.cta{height:158px;background:linear-gradient(90deg,#14142a,#1c1c38 50%,#14142a);text-align:center;color:#fff}
.cta::before{content:"";position:absolute;left:0;top:0;width:100%;height:5px;background:linear-gradient(90deg,var(--orange) 70%,var(--green))}
.cta h2{font-family:'Roboto',sans-serif;font-weight:500;font-size:29px;padding-top:27px;letter-spacing:.5px}
.cta p{font-size:10px;color:#c8c8d4;margin-top:4px}
.cta .row{display:flex;justify-content:center;align-items:center;gap:16px;margin-top:18px}
.cta .phone{font-family:'Barlow Condensed',sans-serif;font-size:23px;color:var(--green)}
.cta .sep{width:2px;height:26px;background:#fff}
.cta .btn{font-size:9px;padding:9px 18px}

/* About */
.about{height:324px;background:var(--grey)}
.about .deco{position:absolute;left:-90px;top:20px;width:300px;height:290px;border-radius:50%;background:#e2e2e2}
.about-left{position:absolute;left:174px;top:106px}
.about-left h2{font-size:19px;font-weight:700;line-height:25px;text-transform:uppercase;margin-top:6px}
.about-divider{position:absolute;left:470px;top:97px;width:1px;height:116px;background:#d6d6d6}
.about-right{position:absolute;left:502px;top:98px;width:510px}
.about-right h3{font-size:11px;font-weight:500}
.about-right p{font-size:9px;line-height:13px;color:var(--muted);margin-top:10px}
.about-right .btn{margin-top:14px}

/* Why us */
.why{height:530px;background:var(--navy)}
.why .media{position:absolute;left:0;top:0;width:591px;height:530px;background:linear-gradient(160deg,#8d8f95,#5a4a44 55%,#3c3a3d)}
.why .badge{position:absolute;left:543px;top:210px;width:96px;height:96px;border-radius:50%;background:var(--navy);border:3px solid #fff}
.why-copy{position:absolute;left:655px;top:70px;width:400px;color:#fff}
.why-copy .eyebrow{color:var(--green)}
.why-copy h2{font-size:23px;line-height:35px;font-weight:700;text-transform:uppercase;margin-top:6px}
.why-copy>p{font-size:9.5px;line-height:13.5px;color:#d2d2dc;margin-top:18px;width:330px}
.feature{display:flex;gap:14px;margin-top:25px}
.feature svg{flex:none;margin-top:2px}
.feature h4{font-size:12px;font-weight:400;color:var(--orange)}
.feature p{font-size:8.5px;line-height:13px;color:#e6e6ee;font-weight:500;margin-top:4px;width:240px}

/* News */
.news{height:659px}
.news .section-head{padding-top:100px}
.news-grid{position:absolute;left:242px;top:218px;display:flex;gap:20px}
.post{width:225px;height:356px;background:var(--grey);border-radius:4px;overflow:hidden;position:relative}
.post .media{height:141px}
.post .date{position:absolute;left:164px;top:117px;width:43px;height:38px;background:var(--orange);color:#fff;font-size:9px;text-align:center;line-height:11px;padding-top:8px}
.post .cat{font-size:8.5px;color:var(--orange);margin:24px 0 0 20px}
.post h3{font-size:13.5px;font-weight:500;line-height:16px;margin:14px 20px 0}
.post p{font-size:8.5px;line-height:13px;color:var(--muted);margin:14px 20px 0}
.post .go{position:absolute;left:20px;bottom:18px;width:42px;height:27px;border-radius:14px;background:var(--orange);color:#fff;font-size:13px;text-align:center;line-height:27px}

/* Contact */
.contact{height:475px;background:#f4f4f4}
.contact-card{position:absolute;left:259px;top:63px;width:222px;height:340px;background:var(--orange);box-shadow:12px 12px 0 var(--green);color:#fff;padding:48px 0 0 14px}
.contact-item{display:flex;gap:14px;margin-bottom:60px}
.contact-item svg{flex:none;margin-top:2px}
.contact-item h4{font-size:17px;font-weight:500}
.contact-item p{font-size:9px;line-height:10px;margin-top:4px}
.contact-form{position:absolute;left:537px;top:86px;width:413px}
.contact-form h2{font-size:15.5px;font-weight:700;text-transform:uppercase;margin-top:6px}
.field{border-bottom:1px solid #bdbdbd;font-size:9px;color:var(--orange);padding-bottom:12px}
.field-row{display:flex;gap:38px;margin-top:32px}
.field-row .field{flex:1}
.contact-form .btn{margin-top:40px;display:inline-flex;align-items:center;gap:8px;padding:7px 14px}

/* Footer */
.footer{height:223px;background:var(--navy);text-align:center;color:#fff}
.footer::before{content:"";position:absolute;left:0;top:0;width:100%;height:5px;background:linear-gradient(90deg,var(--orange) 70%,var(--green))}
.footer nav{display:flex;justify-content:center;gap:24px;font-size:11px;text-transform:uppercase;padding-top:50px}
.footer small{display:block;font-size:9.5px;margin-top:17px}
.footer .brand{justify-content:center;font-size:52px;margin-top:28px}
.footer .brand .dot{width:50px;height:50px}
</style>
</head>
<body>

<header class="hero">
  <div class="hero-visual" role="img" aria-label="Globales Datennetz mit leuchtenden Knotenpunkten über der Erde bei Nacht"></div>
  <div class="hero-base"></div>
  <div class="brand"><span class="dot"></span>nexora</div>
  <nav class="nav">
    <span class="active">Startseite</span><span>Dienstleistungen</span><span>Preis</span><span>Über uns</span><span>Blog</span><span class="kontakt">Kontakt</span>
  </nav>
  <div class="hero-copy">
    <div class="eyebrow">Wir sind ein führendes Technologieunternehmen</div>
    <h1>Integrierte Lösung<br>für das digitale<br>Zeitalter</h1>
    <p>Orem ipsum dolor sit amet, consectetur adipiscing elit utelit tellus, luctus nec ullam corper mattis, pulvinar dapibus leo nulla metus.</p>
  </div>
</header>

<section class="services">
  <div class="section-head">
    <div class="eyebrow">Wir bieten ein breites</div>
    <div class="title">Vielzahl von Digitalisierungslösungen</div>
  </div>
  <div class="service-grid">
    <article class="card"><div class="media" role="img" aria-label="Techniker mit Handschuhen beim Verkabeln" style="background:linear-gradient(135deg,#ddd,#f08a2a 60%,#333)"></div><h3>IT Systemhaus</h3><p>Lorem ipsum dolor sit amet, consectetur adipiscing elit. Ut elit tellus, luctus nec ulla-mcorper mattis, pulvinar dapibus leo.</p><span class="more">Weiterlesen</span></article>
    <article class="card"><div class="media" role="img" aria-label="Laptop mit Software-Symbolen" style="background:linear-gradient(135deg,#c9741f,#3a2a22 60%,#1a1a1a)"></div><h3>Softwareentwicklung</h3><p>Lorem ipsum dolor sit amet, consectetur adipiscing elit. Ut elit tellus, luctus nec ulla-mcorper mattis, pulvinar dapibus leo.</p><span class="more">Weiterlesen</span></article>
    <article class="card"><div class="media" role="img" aria-label="IP-Telefon vor Netzwerk-Switch" style="background:linear-gradient(180deg,#6b7ba8,#3a3f55 60%,#9aa0b4)"></div><h3>IP Telefonsysteme</h3><p>Lorem ipsum dolor sit amet, consectetur adipiscing elit. Ut elit tellus, luctus nec ulla-mcorper mattis, pulvinar dapibus leo.</p><span class="more">Weiterlesen</span></article>
    <article class="card"><div class="media" role="img" aria-label="Sicherheitsschild über einer digitalen Stadt" style="background:linear-gradient(180deg,#1e5fb8,#0d2d66)"></div><h3>Sicherheitstechnik</h3><p>Lorem ipsum dolor sit amet, consectetur adipiscing elit. Ut elit tellus, luctus nec ulla-mcorper mattis, pulvinar dapibus leo.</p><span class="more">Weiterlesen</span></article>
    <article class="card"><div class="media" role="img" aria-label="Laptop mit Cloud-Symbol" style="background:linear-gradient(135deg,#9a8060,#2a2a2a 60%,#5a4a3a)"></div><h3>Clouddiesnste</h3><p>Lorem ipsum dolor sit amet, consectetur adipiscing elit. Ut elit tellus, luctus nec ulla-mcorper mattis, pulvinar dapibus leo.</p><span class="more">Weiterlesen</span></article>
    <article class="card"><div class="media" role="img" aria-label="Serverschränke im Rechenzentrum" style="background:linear-gradient(90deg,#222,#8a8a8a 50%,#222)"></div><h3>Webhosting</h3><p>Lorem ipsum dolor sit amet, consectetur adipiscing elit. Ut elit tellus, luctus nec ulla-mcorper mattis, pulvinar dapibus leo.</p><span class="more">Weiterlesen</span></article>
    <article class="card"><div class="media" role="img" aria-label="Beratungsgespräch mit Dokumenten" style="background:linear-gradient(135deg,#e8ecf2,#9aa4b4)"></div><h3>Consulting</h3><p>Lorem ipsum dolor sit amet, consectetur adipiscing elit. Ut elit tellus, luctus nec ulla-mcorper mattis, pulvinar dapibus leo.</p><span class="more">Weiterlesen</span></article>
    <article class="card"><div class="media" role="img" aria-label="Leuchtendes Glasfaser- und Kupferkabel" style="background:linear-gradient(90deg,#3a3a4a,#d8682a 50%,#f6e8c8 80%,#3a6aa8)"></div><h3>Netzwerktechnik</h3><p>Lorem ipsum dolor sit amet, consectetur adipiscing elit. Ut elit tellus, luctus nec ulla-mcorper mattis, pulvinar dapibus leo.</p><span class="more">Weiterlesen</span></article>
  </div>
</section>

<section class="cta">
  <h2>KOSTENLOSE ERSTBERATUNG</h2>
  <p>Jetzt Termin vereinbaren und 30 Minuten kostenlose Beratung erhalten.</p>
  <div class="row"><span class="phone">+49 30 12 | 345 67-0</span><span class="sep"></span><span class="btn">PLANEN SIE IHR MEETING</span></div>
</section>

<section class="about">
  <div class="deco"></div>
  <div class="about-left">
    <div class="eyebrow">Über unsere Firma</div>
    <h2>Wir helfen Unternehmen,<br>im digitalen Zeitalter<br>voranzukommen</h2>
  </div>
  <div class="about-divider"></div>
  <div class="about-right">
    <h3>Dies ist die Hauptüberschrift</h3>
    <p>Lorem ipsum dolor sit amet, consectetur adipiscing elit, sed do eiusmod tempor incididunt ut labore et dolore magna aliqua. Ut enim ad minim veniam, quis nostrud exercitation ullamco laboris nisi ut aliquip ex ea commodo consequat.</p>
    <span class="btn">View All &nbsp;→</span>
  </div>
</section>

<section class="why">
  <div class="media" role="img" aria-label="Team im Besprechungsraum eines modernen Büros"></div>
  <div class="badge"></div>
  <div class="why-copy">
    <div class="eyebrow">Warum uns wählen</div>
    <h2>Seit über 30 Jahren in<br>der Technologiebranche</h2>
    <p>Lorem ipsum dolor sit amet, consectetur adipiscing elit, sed do eiusmod tempor incididunt ut labore et dolore magna aliqua. Ut enim ad minim veniam, quis nostrud exercitation ullamco laboris nisi ut aliquip ex ea commodo consequat.</p>
    <div class="feature">
      <svg width="28" height="28" viewBox="0 0 28 28" fill="none" stroke="#e8821f" stroke-width="1.6"><circle cx="14" cy="14" r="11"/><circle cx="14" cy="14" r="5"/><path d="M6 6l4 4M22 6l-4 4M6 22l4-4M22 22l-4-4"/></svg>
      <div><h4>Experten für technischen Support</h4><p>Diam vel quam elementum pulvinar ac tium aenean pharetra magna ac placerat quis eget.</p></div>
    </div>
    <div class="feature">
      <svg width="28" height="28" viewBox="0 0 28 28" fill="none" stroke="#e8821f" stroke-width="1.6"><path d="M14 3l3.3 7 7.5.8-5.6 5.1 1.6 7.4L14 19.6l-6.8 3.7 1.6-7.4-5.6-5.1 7.5-.8z"/></svg>
      <div><h4>Solide Teamarbeit</h4><p>Diam vel quam elementum pulvinar ac tium aenean pharetra magna ac placerat quis eget.</p></div>
    </div>
    <div class="feature">
      <svg width="28" height="28" viewBox="0 0 28 28" fill="none" stroke="#e8821f" stroke-width="1.6"><rect x="3" y="3" width="22" height="6" rx="1"/><rect x="3" y="11" width="22" height="6" rx="1"/><rect x="3" y="19" width="22" height="6" rx="1"/><circle cx="7" cy="6" r="1"/><circle cx="7" cy="14" r="1"/><circle cx="7" cy="22" r="1"/></svg>
      <div><h4>Fortschrittliche Technologie</h4><p>Diam vel quam elementum pulvinar ac tium aenean pharetra magna ac placerat quis eget.</p></div>
    </div>
  </div>
</section>

<section class="news">
  <div class="section-head">
    <div class="eyebrow">Bleiben Sie mit nexora auf dem laufenden</div>
    <div class="title">Von den neuesten &amp; beliebten News</div>
  </div>
  <div class="news-grid">
    <article class="post"><div class="media" role="img" aria-label="Nahaufnahme einer Industriemaschine" style="background:linear-gradient(135deg,#555,#bbb 50%,#333)"></div><div class="date">July 19<br>2021</div><div class="cat">▭ Atrificial Store</div><h3>Repeated of endeavor mr position kindness.</h3><p>Lorem ipsum dolor sit amet, consectetur adipiscing elit, sed do eiusmod tempor incid-idunt ut labore.</p><span class="go">→</span></article>
    <article class="post"><div class="media" role="img" aria-label="Zwei Techniker in einer Werkstatt" style="background:linear-gradient(135deg,#7a8aa0,#3a6a9a 50%,#c8a070)"></div><div class="date">July 19<br>2021</div><div class="cat">▭ Automation</div><h3>Justifying Automation in Your Factory.</h3><p>Lorem ipsum dolor sit amet, consectetur adipiscing elit, sed do eiusmod tempor incid-idunt ut labore.</p><span class="go">→</span></article>
    <article class="post"><div class="media" role="img" aria-label="Roboterarm in einer Produktionshalle" style="background:linear-gradient(135deg,#ddd,#888 50%,#444)"></div><div class="date">July 19<br>2021</div><div class="cat">▭ Digitalization</div><h3>Boost Your Cobot Safety Know-How with These Digital Resources</h3><p>Lorem ipsum dolor sit amet, consectetur adipiscing elit, sed do eiusmod tempor incid-idunt ut labore.</p><span class="go">→</span></article>
  </div>
</section>

<section class="contact">
  <div class="contact-card">
    <div class="contact-item">
      <svg width="26" height="26" viewBox="0 0 26 26" fill="#fff"><path d="M13 2a7 7 0 0 0-7 7c0 5 7 14 7 14s7-9 7-14a7 7 0 0 0-7-7zm0 10a3 3 0 1 1 0-6 3 3 0 0 1 0 6z"/></svg>
      <div><h4>Nexora GmbH</h4><p>Lindenallee 12<br>10115 Berlin</p></div>
    </div>
    <div class="contact-item">
      <svg width="26" height="26" viewBox="0 0 26 26" fill="#fff"><path d="M7 3l4 5-2.5 2.5c1.3 2.8 3.2 4.7 6 6L17 14l5 4-2.5 4C11 22 4 15 3 6.5z"/></svg>
      <div><h4>Einen Anruf tätigen</h4><p>+49 30 12 | 345 67-0</p></div>
    </div>
    <div class="contact-item">
      <svg width="26" height="26" viewBox="0 0 26 26" fill="none" stroke="#fff" stroke-width="2"><rect x="3" y="6" width="20" height="14"/><path d="M3 6l10 8 10-8"/></svg>
      <div><h4>Senden Sie eine E-Mail</h4><p>vertrieb@nexora.de</p></div>
    </div>
  </div>
  <div class="contact-form">
    <div class="eyebrow">Wir freuen uns jederzeit von Ihnen zu hören</div>
    <h2>Machen Sie sich bereit, Ihr Projekt mit uns zu starten</h2>
    <div class="field" style="margin-top:30px">Name</div>
    <div class="field-row"><div class="field">Email*</div><div class="field">Phone</div></div>
    <div class="field" style="margin-top:32px;height:110px">Tell Us About Project*</div>
    <span class="btn">Send Message
      <svg width="14" height="12" viewBox="0 0 14 12" fill="#fff"><path d="M0 5l14-5-4 12-3-5z"/></svg>
    </span>
  </div>
</section>

<footer class="footer">
  <nav><span>Startseite</span><span>Dienstleistungen</span><span>Preis</span><span>Über uns</span><span>Blog</span><span>Kontakt</span></nav>
  <small>COPYRIGHT © 2021. ALL RIGHTS RESERVED.</small>
  <div class="brand"><span class="dot"></span>nexora</div>
</footer>

</body>
</html>
```